Postcard Design

We are Brightmoor Care. A new way of providing quality healthcare for less. We offer a monthly membership program for $77 per person, $167 per family and cover about 85% of medical conditions. Medical office visits are just $7 each. This innovative program have already saved millions of dollars for it's members in health care costs. We are inviting people to a brief, educational meeting to learn more about how they can save money on their healthcare. We need something catchy and upbeat, positive with 1-2 photos inviting them to come find out more. We will be having appetizers. The date is Wednesday, Feb. 18 drop by between 6-8 pm
Industry/Entity Type
Healthcare

```html
<!DOCTYPE html>
<html lang="en">
<head>
<meta charset="utf-8">
<title>Brightmoor Care – Postcard</title>
<link href="https://fonts.googleapis.com/css2?family=PT+Sans+Narrow:wght@400;700&family=Source+Sans+3:ital,wght@0,400;0,600;0,700;1,600&display=swap" rel="stylesheet">
<style>
  :root {
    --orange: #f7962e;
    --blue: #1b87b8;
    --deep-blue: #1a75a8;
    --mint: #abddd4;
    --grey: #c7c8ca;
    --ink: #2b1d12;
    --white: #ffffff;
    --line: #b9bcbf;
    --page: #ece7df;
  }
  * { margin: 0; padding: 0; box-sizing: border-box; }
  html, body { width: 1200px; height: 500px; overflow: hidden; }
  body {
    background: var(--page);
    position: relative;
    font-family: "PT Sans Narrow", "Source Sans 3", sans-serif;
  }
  .card { position: absolute; top: 33px; width: 555px; height: 433px; overflow: hidden; background: var(--white); }
  .card--front { left: 30px; background: var(--mint); }
  .card--back { left: 618px; width: 552px; }
  .layer { position: absolute; inset: 0; }

  /* front */
  .invite {
    position: absolute; top: 16px; left: 0; width: 100%;
    text-align: center; color: var(--white); font-size: 23px;
  }
  .headline {
    position: absolute; top: 44px; left: 0; width: 100%;
    text-align: center; color: var(--ink);
    font-family: "Source Sans 3", sans-serif; font-weight: 700; font-size: 42px; letter-spacing: -0.3px;
  }
  .subline {
    position: absolute; top: 94px; left: 68px; color: var(--white);
    font-family: "Source Sans 3", sans-serif; font-style: italic; font-weight: 600; font-size: 16px; line-height: 20px;
  }
  .event {
    position: absolute; top: 174px; left: 40px; width: 240px;
    text-align: center; color: var(--ink); font-size: 19px; line-height: 21px;
  }
  .event__date { font-weight: 700; font-size: 20px; }
  .photo-doctors {
    position: absolute; left: 40px; top: 237px; width: 236px; height: 186px;
    background: linear-gradient(160deg, #d9dcd6 0%, #c3c7c2 45%, #a9b6c3 100%);
  }
  .photo-baby {
    position: absolute; left: 305px; top: 100px; width: 250px; height: 260px;
    background: radial-gradient(ellipse at 40% 45%, #f3d8c6 0%, #e8c2aa 45%, #dcdad8 80%);
  }
  .brand {
    position: absolute; display: flex; flex-direction: column; align-items: center;
    font-family: "Source Sans 3", sans-serif; font-weight: 700; color: var(--blue); text-align: center;
  }
  .brand__dot { border-radius: 50%; background: var(--blue); flex: none; }
  .brand--front { left: 375px; top: 300px; width: 170px; font-size: 26px; line-height: 28px; gap: 6px; }
  .brand--front .brand__dot { width: 44px; height: 44px; }

  /* back */
  .panel { position: absolute; left: 0; top: 0; width: 285px; height: 357px; }
  .panel__intro {
    position: absolute; top: 24px; left: 20px; width: 245px;
    color: var(--ink); font-weight: 700; font-size: 17px; line-height: 21px;
  }
  .panel__offer {
    position: absolute; top: 148px; left: 14px; width: 265px;
    color: var(--white); font-weight: 700; font-size: 15.5px; line-height: 19px;
  }
  .offer-list { list-style: none; margin-top: 2px; }
  .offer-list li { display: flex; align-items: center; gap: 4px; }
  .offer-list svg { width: 10px; height: 10px; flex: none; }
  .contact {
    position: absolute; top: 262px; left: 0; width: 285px; text-align: center; color: var(--white);
    font-weight: 700; font-size: 15.5px;
  }
  .contact__phone {
    display: flex; justify-content: center; align-items: center; gap: 4px;
    color: var(--orange); font-family: "Source Sans 3", sans-serif; font-size: 23px; margin-top: 4px;
  }
  .contact__phone svg { width: 18px; height: 18px; }
  .web {
    position: absolute; top: 319px; left: 0; width: 285px; height: 38px; line-height: 38px;
    text-align: center; color: var(--ink); font-family: "Source Sans 3", sans-serif; font-weight: 700; font-size: 21px;
  }
  .brand--back { left: 298px; top: 22px; width: 150px; font-size: 17px; line-height: 20px; gap: 5px; }
  .brand--back .brand__dot { width: 32px; height: 32px; }
  .stamp { position: absolute; left: 459px; top: 10px; width: 80px; height: 82px; border: 1px solid var(--line); }
  .address-line { position: absolute; left: 322px; width: 220px; height: 1px; background: var(--line); }
</style>
</head>
<body>

<section class="card card--front">
  <div class="photo-baby" role="img" aria-label="Photo of a baby being examined with a stethoscope"></div>
  <svg class="layer" viewBox="0 0 555 433" preserveAspectRatio="none" aria-hidden="true">
    <path d="M0 0 H555 V132 C490 124 430 124 330 130 C240 136 140 140 0 158 Z" fill="var(--orange)"/>
    <path d="M0 158 C140 140 240 136 330 130 C430 124 490 124 555 132" fill="none" stroke="var(--deep-blue)" stroke-width="4"/>
    <path d="M300 433 C310 370 360 300 555 278 V433 Z" fill="var(--grey)"/>
  </svg>
  <p class="invite">You are cordially invited to a brief educational meeting on</p>
  <h1 class="headline">Quality Healthcare For Less</h1>
  <p class="subline">Find out how you can save<br>money on your healthcare</p>
  <div class="event">
    <p class="event__date">Wednesday, Feb. 18</p>
    <p>Drop by for appetizers<br>between 6-8 pm</p>
  </div>
  <div class="photo-doctors" role="img" aria-label="Photo of two doctors talking with a patient in a hospital bed"></div>
  <div class="brand brand--front"><span class="brand__dot"></span><span class="brand__name">Brightmoor Care</span></div>
</section>

<section class="card card--back">
  <svg class="panel" viewBox="0 0 285 357" preserveAspectRatio="none" aria-hidden="true">
    <rect width="285" height="357" fill="var(--blue)"/>
    <path d="M0 0 H285 V96 C220 112 150 102 80 106 C40 108 15 112 0 116 Z" fill="var(--orange)"/>
    <path d="M0 116 C15 112 40 108 80 106 C150 102 220 112 285 96" fill="none" stroke="var(--white)" stroke-width="6"/>
    <rect y="317" width="285" height="40" fill="var(--orange)"/>
  </svg>
  <p class="panel__intro">An innovative program that have already saved millions of dollars for it's members in health care costs</p>
  <div class="panel__offer">
    <p>&nbsp;&nbsp;&nbsp;We offer a monthly membership program<br>&nbsp;&nbsp;&nbsp;that cover about 85% of medical conditions.</p>
    <ul class="offer-list">
      <li><svg viewBox="0 0 10 10"><path d="M5 0 6.2 3.6H10L7 5.8 8.1 9.5 5 7.3 1.9 9.5 3 5.8 0 3.6H3.8Z" fill="var(--orange)"/></svg>$77 per person</li>
      <li><svg viewBox="0 0 10 10"><path d="M5 0 6.2 3.6H10L7 5.8 8.1 9.5 5 7.3 1.9 9.5 3 5.8 0 3.6H3.8Z" fill="var(--orange)"/></svg>$167 per family</li>
      <li><svg viewBox="0 0 10 10"><path d="M5 0 6.2 3.6H10L7 5.8 8.1 9.5 5 7.3 1.9 9.5 3 5.8 0 3.6H3.8Z" fill="var(--orange)"/></svg>Medical office visits are just $7 each.</li>
    </ul>
  </div>
  <div class="contact">
    <p>For more information, Call:</p>
    <p class="contact__phone">
      <svg viewBox="0 0 20 20" aria-hidden="true"><circle cx="10" cy="10" r="9" fill="none" stroke="var(--orange)" stroke-width="2"/><path d="M7 5.5 9 7.5 8 9c.6 1.2 1.6 2.2 2.8 2.8l1.5-1 2 2-1.3 1.7C9.5 14.3 5.7 10.5 5.5 7Z" fill="var(--orange)"/></svg>
      555.214.0386
    </p>
  </div>
  <p class="web">www.brightmoorcare.com</p>

  <div class="brand brand--back"><span class="brand__dot"></span><span class="brand__name">Brightmoor Care</span></div>
  <div class="stamp"></div>
  <div class="address-line" style="top:201px"></div>
  <div class="address-line" style="top:236px"></div>
  <div class="address-line" style="top:271px"></div>
  <div class="address-line" style="top:306px"></div>
</section>

</body>
</html>
```